Business card design needed

New company in Executive Search & Consulting (Recruitment & Head Hunting Company)

We recruit IT, Accounting & Finance, Human Resources and Senior Management

with offices in Perth, Brisbane, Seoul and Hong Kong

Industry/Entity Type

Business

Contact Information for Business Card

Calderwood-Ashfield Executive Search & Consulting
*Perth *Brisbane * Seoul * Hong Kong
Neil Calderwood Australian Director
147 Mellor Street Subiaco Western Australia
www.calderwoodashfield.example.au
Ph: 08 6000 4827 Fax: 08 6000 9153
Mobile: 0400 731 562

```html
<!DOCTYPE html>
<html lang="en">
<head>
<meta charset="utf-8">
<title>Calderwood-Ashfield Business Card</title>
<link rel="stylesheet" href="https://fonts.googleapis.com/css2?family=Lato:wght@300;400&display=swap">
<style>
  :root {
    --backdrop: #1c1c1d;
    --card: #ffffff;
    --ink: #55575e;
    --ink-soft: #7c7e85;
    --bar: #6c6f78;
    --mark: #8a8d95;
  }
  * { box-sizing: border-box; margin: 0; padding: 0; }
  html, body {
    width: 1200px; height: 1200px; overflow: hidden;
    background: var(--backdrop);
    font-family: "Lato", Arial, sans-serif;
    font-weight: 300;
    color: var(--ink);
  }
  .stage {
    width: 1200px; height: 1200px;
    display: flex; flex-direction: column;
    align-items: center; justify-content: center; gap: 70px;
  }
  .card {
    position: relative;
    width: 760px; height: 434px;
    background: var(--card);
    box-shadow: 0 10px 30px rgba(0,0,0,.5);
  }

  /* Back of card */
  .card-back .brand {
    position: absolute; left: 0; right: 0; top: 160px;
    display: flex; align-items: center; justify-content: center; gap: 14px;
  }
  .brand-square { width: 22px; height: 22px; background: var(--mark); }
  .brand-name {
    font-size: 30px; font-weight: 400; letter-spacing: 2px;
    text-transform: uppercase; color: var(--ink);
  }
  .card-back .web {
    position: absolute; right: 44px; bottom: 34px;
    font-size: 17px; font-weight: 400; color: var(--ink);
  }

  /* Front of card */
  .contact { position: absolute; left: 52px; top: 40px; }
  .person { font-size: 24px; letter-spacing: 3px; text-transform: uppercase; color: var(--ink-soft); }
  .person .role { font-size: 15px; letter-spacing: 1px; text-transform: none; margin-left: 8px; }
  .contact-lines { margin-top: 6px; font-size: 15px; line-height: 1.35; color: var(--ink); }
  .divider {
    position: absolute; left: 52px; right: 52px; top: 190px;
    height: 11px; background: var(--bar);
  }
  .lockup { position: absolute; left: 52px; top: 232px; }
  .lockup .brand { display: flex; align-items: center; gap: 12px; }
  .lockup .brand-name { font-size: 27px; }
  .tagline { margin-top: 6px; font-size: 14px; letter-spacing: 2px; text-transform: uppercase; color: var(--ink-soft); }
  .offices { margin-top: 8px; font-size: 12px; letter-spacing: 2px; text-transform: uppercase; color: var(--ink); }
  .address { position: absolute; left: 52px; bottom: 34px; font-size: 16px; color: var(--ink-soft); }
</style>
</head>
<body>
<main class="stage">
  <section class="card card-back">
    <div class="brand">
      <span class="brand-square"></span>
      <span class="brand-name">Calderwood-Ashfield</span>
    </div>
    <p class="web">www.calderwoodashfield.example.au</p>
  </section>

  <section class="card card-front">
    <div class="contact">
      <p class="person">Neil Calderwood<span class="role">Australian Director</span></p>
      <p class="contact-lines">
        Phone: 08 6000 4827<br>
        Fax: 08 6000 9153<br>
        Mobile: 0400 731 562<br>
        www.calderwoodashfield.example.au
      </p>
    </div>
    <div class="divider"></div>
    <div class="lockup">
      <div class="brand">
        <span class="brand-square"></span>
        <span class="brand-name">Calderwood-Ashfield</span>
      </div>
      <p class="tagline">Executive Search &amp; Consulting</p>
      <p class="offices">Perth &bull; Brisbane &bull; Seoul &bull; Hong Kong</p>
    </div>
    <p class="address">147 Mellor Street Subiaco Western Australia</p>
  </section>
</main>
</body>
</html>
```